Agricultural Consulting Website

Provide a modern yet business like website for my new Agriculture Consulting Business in Australia called FieldNorth. Whilst we are based in Australia we are targetting both domestic and international markets (especially in Asia). We are targetting corporate, small business, government and farmer clients. The design should compliment our logo also sourced through pixel harbor. The webiste should be easy for me to keep updated on a regular basis without the need to go back to the designer.

Industry/Entity Type

Business

Requirements
Must have
• clean crisp feel
• be modern yet business like
• be able to be updated by myself easily

```html
<!DOCTYPE html>
<html lang="en">
<head>
<meta charset="utf-8">
<title>FieldNorth – Agricultural Consulting</title>
<link href="https://fonts.googleapis.com/css2?family=Roboto:wght@300;400;500&display=swap" rel="stylesheet">
<style>
:root{
  --green:#5f8f1f;
  --green-bright:#6ea21f;
  --footer-green:#4f8420;
  --brown:#5a3203;
  --brown-dark:#4a2a05;
  --text:#333;
  --muted:#555;
  --line:#d9d9d9;
  --nav-bg:#f4f4f4;
}
*{box-sizing:border-box;margin:0;padding:0}
html,body{width:1144px;height:1200px;overflow:hidden}
body{font-family:'Roboto',sans-serif;font-weight:300;color:var(--text);background:#fff;position:relative}
a{color:inherit;text-decoration:none}

.top-strip{position:absolute;top:0;left:0;width:1144px;height:4px;
  background:repeating-linear-gradient(90deg,var(--brown) 0 50px,var(--green-bright) 50px 200px)}
.site-header{position:absolute;top:4px;left:0;width:1144px;height:84px}
.brand{position:absolute;left:23px;top:16px;display:flex;align-items:center;gap:8px}
.brand-mark{width:52px;height:52px;background:var(--brown)}
.brand-name{font-size:34px;font-weight:400;color:var(--green-bright);letter-spacing:-.5px}
.call{position:absolute;right:22px;top:22px;color:var(--brown);font-size:21px;font-weight:300}
.call strong{font-weight:300;color:var(--green);font-size:32px;margin-left:2px}

.main-nav{position:absolute;top:88px;left:0;width:1144px;height:42px;background:var(--nav-bg);
  border-top:1px solid var(--line);border-bottom:1px solid var(--line);display:flex}
.main-nav a{display:flex;align-items:center;justify-content:center;font-size:14px;font-weight:300;color:#333;border-right:1px solid var(--line);height:100%}
.main-nav a.login{border-right:none;color:var(--brown);font-weight:400;gap:6px}

.hero{position:absolute;top:130px;left:0;width:1144px;height:414px;
  background:linear-gradient(180deg,#b99d74 0%,#a88b60 30%,#8a7a4c 45%,#c98a3a 60%,#b8702a 100%)}
.hero-tractor{position:absolute;left:520px;top:95px;width:440px;height:300px;
  background:linear-gradient(160deg,#2d6a26,#1f4a1a);border-radius:20px;opacity:.75}
.hero-kicker{position:absolute;left:22px;top:92px;background:rgba(30,25,20,.85);color:#fff;font-size:25px;font-weight:300;padding:0 5px;height:34px;line-height:34px}
.hero-title{position:absolute;left:22px;top:130px;background:rgba(30,25,20,.85);color:#fff;font-size:44px;font-weight:400;padding:0 6px;height:48px;line-height:50px;letter-spacing:-.3px}
.slider-bar{position:absolute;top:543px;left:0;width:1144px;height:4px;background:var(--green-bright)}
.slider-tab{position:absolute;top:522px;left:528px;width:88px;height:24px;background:var(--green-bright);border-radius:14px 14px 0 0;display:flex;justify-content:center;align-items:center;gap:8px;padding-top:2px}
.slider-tab span{width:8px;height:8px;border-radius:50%;background:#fff}

.audiences{position:absolute;top:547px;left:0;width:1144px;height:107px;display:flex;border-bottom:1px solid var(--line)}
.audience{position:relative;height:100%;border-right:2px solid #e2e2e2;background:linear-gradient(#fff,#ececec);padding:28px 0 0 22px}
.audience:last-child{border-right:none}
.audience h3{font-size:20px;font-weight:300;color:var(--green)}
.audience p{font-size:14px;color:var(--muted);width:145px;line-height:17px;margin-top:0}
.audience .art{position:absolute;top:10px;width:90px;height:88px;border-radius:8px}

.welcome{position:absolute;left:22px;top:683px;width:565px}
h2{font-size:21px;font-weight:300;color:#222;margin-bottom:7px;line-height:25px}
.welcome p{font-size:14px;line-height:18px;color:var(--muted);margin-bottom:9px;letter-spacing:-.2px}
.more{font-size:12px;color:var(--green-bright);font-weight:400}
.welcome .more{display:block;margin-top:14px}
.news{position:absolute;left:675px;top:683px;width:450px}
.news-item{display:flex;padding:4px 0 10px 0}
.news-item+.news-item{border-top:1px dotted #bbb;padding-top:12px}
.date{flex:0 0 98px;width:98px;text-align:center;line-height:1}
.date b{display:block;font-size:44px;font-weight:300;color:var(--brown-dark)}
.date i{display:block;font-style:normal;font-size:26px;font-weight:300;color:var(--green)}
.news-body{flex:1}
.news-item p{font-size:14px;line-height:18px;color:var(--muted);letter-spacing:-.2px}
.news-item .more{display:block;margin-top:2px}

.badges{position:absolute;top:898px;left:0;width:1144px;height:84px;display:flex;border-top:1px solid var(--line)}
.badges li{list-style:none;border-right:1px solid var(--line);display:flex;align-items:center;justify-content:center;height:100%}
.badge{background:#9a9a9a;opacity:.7}

.site-footer{position:absolute;top:982px;left:0;width:1144px;height:168px;background:var(--footer-green);color:#fff}
.site-footer h4{font-size:17px;font-weight:300;margin-bottom:10px}
.testimonial{position:absolute;left:23px;top:24px;width:445px;font-size:13px;line-height:18.5px;font-weight:400;letter-spacing:-.15px}
.testimonial cite{display:block;font-style:normal;margin-top:7px}
.contact{position:absolute;left:575px;top:24px;font-size:13px;font-weight:400}
.contact li{list-style:none;display:flex;align-items:center;gap:6px;margin-bottom:6px}
.social{display:flex;gap:18px;margin:10px 0 0 9px}
.social span{width:15px;height:15px;border-radius:50%;border:2px solid #fff;opacity:.9}
.newsletter{position:absolute;left:887px;top:24px;width:245px;font-size:12.5px;font-weight:400;letter-spacing:-.2px}
.newsletter input{display:block;margin-top:12px;width:234px;height:30px;border:none;padding:0 10px;font-family:inherit;font-size:12px;color:#888}
.newsletter button{position:absolute;right:6px;top:101px;background:var(--brown);color:#fff;border:none;border-radius:12px;padding:3px 6px;font-family:inherit;font-size:13px}

.bottom-bar{position:absolute;top:1150px;left:0;width:1144px;height:50px;background:var(--brown);color:#fff;font-size:13px;font-weight:400;display:flex;justify-content:space-between;align-items:center;padding:0 22px 0 23px}
</style>
</head>
<body>
<div class="top-strip"></div>

<header class="site-header">
  <a class="brand" href="#"><span class="brand-mark"></span><span class="brand-name">FieldNorth</span></a>
  <div class="call">Call Now: <strong>+11 200 555 0142</strong></div>
</header>

<nav class="main-nav">
  <a href="#" style="width:158px">Home</a>
  <a href="#" style="width:156px">About Us</a>
  <a href="#" style="width:163px">Our Services</a>
  <a href="#" style="width:130px">News</a>
  <a href="#" style="width:161px">Our Clients</a>
  <a href="#" style="width:174px">Contact Us</a>
  <a href="#" class="login" style="width:202px">
    <svg width="16" height="14" viewBox="0 0 16 14"><rect x="1" y="1" width="14" height="9" fill="none" stroke="#5a3203" stroke-width="2"/><rect x="5" y="11" width="6" height="2" fill="#5a3203"/></svg>Log In</a>
</nav>

<section class="hero" role="img" aria-label="Photo of a green tractor working a golden harvested field under a cloudy sky">
  <div class="hero-tractor"></div>
  <div class="hero-kicker">Our Aim is</div>
  <h1 class="hero-title">TO GROW WITH YOU</h1>
</section>
<div class="slider-bar"></div>
<div class="slider-tab"><span></span><span></span><span></span></div>

<section class="audiences">
  <div class="audience" style="width:288px"><h3>Corporate</h3><p>Lorem Ipsum is simply dummy text.</p>
    <div class="art" role="img" aria-label="Illustration of a businessman in a suit" style="left:180px;background:radial-gradient(circle,#f4e6b0,#2a2f3a 70%)"></div></div>
  <div class="audience" style="width:284px"><h3>Small Business</h3><p>Lorem Ipsum is simply dummy text.</p>
    <div class="art" role="img" aria-label="Icon of an office building on a green tile" style="left:185px;background:linear-gradient(#a6d98a,#6cb54a)"></div></div>
  <div class="audience" style="width:285px"><h3>Government</h3><p>Lorem Ipsum is simply dummy text.</p>
    <div class="art" role="img" aria-label="Illustration of a domed government building" style="left:175px;background:linear-gradient(#e6e6e6,#9a9a9a)"></div></div>
  <div class="audience" style="width:287px"><h3>Farmer</h3><p style="width:110px">Lorem Ipsum is simply dummy text.</p>
    <div class="art" role="img" aria-label="Illustration of a farmer in a hat with a seedling" style="left:165px;background:linear-gradient(#b9d98a,#7a6a3a)"></div></div>
</section>

<section class="welcome">
  <h2>Welcome to Our Website:</h2>
  <p>Lorem Ipsum is simply dummy text of the printing and typesetting industry. Lorem Ipsum has been the industry's standard dummy text ever since the 1500s, when an unknown printer took a galley of type and scrambled it to make a type specimen book. It has survived not only five centuries, but also the leap into electronic typesetting, remaining essentially unchanged.</p>
  <p>It was popularised in the 1960s with the release of Letraset sheets containing Lorem Ipsum passages, and more recently with desktop publishing software like Aldus PageMaker including versions of Lorem Ipsum.</p>
  <a class="more" href="#">+Read More</a>
</section>

<section class="news">
  <h2>Latest News:</h2>
  <article class="news-item"><div class="date"><b>26</b><i>Nov</i></div>
    <div class="news-body"><p>Lorem Ipsum is simply dummy text of the printing and typesetting industry. Lorem Ipsum has been the industry's standard dummy text ever since the 1500s.</p><a class="more" href="#">+Read More</a></div></article>
  <article class="news-item"><div class="date"><b>25</b><i>Nov</i></div>
    <div class="news-body"><p>Lorem Ipsum is simply dummy text of the printing and typesetting industry. Lorem Ipsum has been the industry's standard dummy text ever since the 1500s.</p><a class="more" href="#">+Read More</a></div></article>
</section>

<ul class="badges" aria-label="Accreditations">
  <li style="width:150px"><span class="badge" style="width:80px;height:36px;border-radius:18px"></span></li>
  <li style="width:150px"><span class="badge" style="width:96px;height:30px"></span></li>
  <li style="width:149px"><span class="badge" style="width:46px;height:30px;border-radius:50%"></span></li>
  <li style="width:146px"><span class="badge" style="width:36px;height:36px;border-radius:50%"></span></li>
  <li style="width:180px"><span class="badge" style="width:36px;height:36px"></span></li>
  <li style="width:195px"><span class="badge" style="width:112px;height:38px;border-radius:4px"></span></li>
  <li style="width:174px;border-right:none"><span class="badge" style="width:80px;height:36px;border-radius:18px"></span></li>
</ul>

<footer class="site-footer">
  <div class="testimonial">
    <h4>What Our Clients Says:</h4>
    <p>Lorem Ipsum is simply dummy text of the printing and typesetting industry. Lorem Ipsum has been the industry's standard dummy text ever since the 1500s, when an unknown printer took a galley of type and scrambled it to make a type specimen book.</p>
    <cite>Lena Ashby | C.E.O</cite>
  </div>
  <div class="contact">
    <h4>Contact Now</h4>
    <ul>
      <li><svg width="13" height="10" viewBox="0 0 13 10"><rect x=".5" y=".5" width="12" height="9" fill="none" stroke="#fff"/><path d="M.5 .5 6.5 5.5 12.5 .5" fill="none" stroke="#fff"/></svg>Dummy Address, Dummy Street, AU</li>
      <li><svg width="13" height="13" viewBox="0 0 13 13"><path d="M3 1 5 4 4 5.5Q5.5 8 7.5 9L9 8l3 2-1.5 2Q5 11.5 1 2.5Z" fill="#fff"/></svg>Call+11 200 555 0142</li>
      <li><svg width="13" height="13" viewBox="0 0 13 13"><circle cx="6.5" cy="6.5" r="5.8" fill="none" stroke="#fff"/><ellipse cx="6.5" cy="6.5" rx="2.5" ry="5.8" fill="none" stroke="#fff"/><path d="M.7 6.5h11.6" stroke="#fff"/></svg>info@fieldnorth.com.au</li>
    </ul>
    <div class="social"><span></span><span></span><span></span><span></span><span></span></div>
  </div>
  <div class="newsletter">
    <h4>Subscribe to Our Newsletter:</h4>
    <p>Subscribe now to get latest news/updates.</p>
    <input type="email" placeholder="Enter Email">
    <button type="button">Subscribe</button>
  </div>
</footer>

<div class="bottom-bar">
  <span>Copyright © 2013 FieldNorth | All Rights Reserved.</span>
  <span>Home | &nbsp;About Us | Contact Us</span>
</div>
</body>
</html>
```